Get your icon design on millions of velora phones

We're looking for app icon for an velora app which provides backup, transfer and recover. App saves data to cloud (Cratevault, Shelf, Tin etc)) and maintains timeline of activity - so you can go back to snapshot at previous date.
Themes - backup transfer recover, save to cloud.
Also, we're looking for an icon set for categories that are included in backup operation:-
Messages,
Call log,
Photos,
Videos
Contacts
Music
Settings
These icons will have badges applied to indicate status. Sample using velora KLTM icons as per attached screenshot image. (Different brands use their own stylised icons for apps such as messages). Also as per screenshot the icons can be monochromed to show disabled state. So, icons that fill required. See sample tekmo icons attached - we'll apply badges on top left or top right. e.g. green tick in top left corner for all data safe. Items count in top right if there are changes to upload.
People who care about losing details on their phone such as call log, messages, photos. More often 30-45 year old males who buy an expensive smartphone.
Velora

```html
<!DOCTYPE html>
<html lang="en">
<head>
<meta charset="utf-8">
<title>Velora Backup – App Icon and Category Icon Set</title>
<link rel="stylesheet" href="https://fonts.googleapis.com/css2?family=Roboto:wght@400;500&display=swap">
<style>
  :root {
    --blue: #1e9fd2;
    --ink: #333333;
    --label: #222222;
    --bar-black: #000000;
    --bar-dark: #222222;
    --card: #ffffff;
    --card-edge: #d6d6d6;
    --track: #e4e4e4;
    --white: #ffffff;
  }
  * { box-sizing: border-box; margin: 0; padding: 0; }
  html, body { width: 1200px; height: 850px; overflow: hidden; background: var(--white); }
  body { font-family: "Roboto", Arial, sans-serif; }
  .stage { position: relative; width: 1225px; height: 864px; transform: scale(0.98); transform-origin: 0 0; }

  .icon-set { position: absolute; left: 0; top: 0; width: 340px; height: 600px; }
  .set-icon { position: absolute; fill: var(--blue); }
  .set-label { position: absolute; font-size: 15px; color: var(--label); text-align: center; width: 100px; }
  .or { position: absolute; font-size: 11px; font-style: italic; color: var(--label); width: 40px; text-align: center; }

  .screen { position: absolute; left: 345px; top: 84px; width: 486px; height: 670px;
            background: linear-gradient(#f2f2f2 80%, rgba(255,255,255,0)); }
  .status-bar { height: 33px; background: var(--bar-black); display: flex; justify-content: flex-end;
                align-items: center; gap: 6px; padding-right: 8px; }
  .status-time { color: var(--blue); font-size: 20px; }
  .action-bar { height: 66px; background: var(--bar-dark); display: flex; align-items: center; position: relative;
                box-shadow: 0 2px 3px rgba(0,0,0,.3); }
  .done { display: flex; align-items: center; gap: 14px; color: var(--white); font-weight: 500; font-size: 16px; padding-left: 20px; }
  .divider { position: absolute; left: 156px; top: 18px; width: 1px; height: 30px; background: #555; }
  .overflow { position: absolute; right: 34px; top: 17px; }
  .overflow span { display: block; width: 6px; height: 6px; background: #8a8a8a; margin-bottom: 4px; }

  .setting-list { list-style: none; padding: 0 8px; }
  .setting-row { height: 81px; background: var(--card); border-bottom: 3px solid var(--card-edge);
                 display: flex; align-items: center; position: relative; }
  .row-icon { width: 62px; display: flex; justify-content: center; margin-left: 8px; fill: var(--blue); }
  .row-label { margin-left: 18px; font-size: 18px; color: var(--ink); }
  .toggle { position: absolute; left: 331px; top: 24px; width: 129px; height: 32px; background: var(--track); }
  .toggle-on { position: absolute; right: 1px; top: 1px; width: 62px; height: 30px; background: var(--blue);
               color: var(--white); font-size: 16px; display: flex; align-items: center; justify-content: center; }

  .app-icon { position: absolute; width: 345px; height: 345px; }
  .app-icon.framed { left: 875px; top: 145px; border-radius: 72px; padding: 20px;
                     background: linear-gradient(#f6f7f8, #b5b8bb); }
  .app-icon.plain { left: 875px; top: 540px; }
  .icon-tile { width: 100%; height: 100%; border-radius: 56px;
               background: linear-gradient(#a8dbe8 0%, #1fa4d4 22%, #1585b6 100%);
               display: flex; align-items: center; justify-content: center; }
  .plain .icon-tile { border-radius: 66px; }
  .icon-name { color: var(--white); font-size: 44px; font-weight: 500; }
</style>
</head>
<body>
<div class="stage">

  <section class="icon-set" aria-label="Backup category icons">
    <svg class="set-icon" style="left:5px;top:260px" width="48" height="46" viewBox="0 0 48 46">
      <path d="M24,2 L47,18 V45 H1 V18 Z"/>
      <path d="M4,21 L24,36 L44,21" fill="none" stroke="#fff" stroke-width="2.5"/>
    </svg>
    <div class="or" style="left:10px;top:311px">or</div>
    <svg class="set-icon" style="left:5px;top:336px" width="50" height="36" viewBox="0 0 50 36">
      <rect x="1.5" y="1.5" width="47" height="33" fill="none" stroke="#1e9fd2" stroke-width="3"/>
      <path d="M2,3 L25,22 L48,3 M2,33 L19,17 M48,33 L31,17" fill="none" stroke="#1e9fd2" stroke-width="2.5"/>
    </svg>
    <div class="set-label" style="left:-20px;top:383px">Message</div>

    <svg class="set-icon" style="left:100px;top:328px" width="40" height="48" viewBox="0 0 40 48">
      <path d="M7,2 L14,2 L17,13 L12,17 Q16,29 25,36 L30,32 L39,37 L37,45 Q33,48 26,45 Q8,35 3,14 Q2,6 7,2 Z"/>
    </svg>
    <div class="set-label" style="left:70px;top:383px">Call Log</div>

    <svg class="set-icon" style="left:189px;top:335px" width="46" height="36" viewBox="0 0 46 36">
      <rect x="1" y="1" width="36" height="26" fill="none" stroke="#1e9fd2" stroke-width="2"/>
      <rect x="8" y="8" width="37" height="27" fill="#fff" stroke="#1e9fd2" stroke-width="2"/>
      <path d="M11,32 L21,22 L27,27 L33,20 L42,32 Z"/>
      <circle cx="18" cy="16" r="3"/>
    </svg>
    <div class="set-label" style="left:162px;top:383px">Photos</div>

    <svg class="set-icon" style="left:280px;top:190px" width="46" height="46" viewBox="0 0 46 46">
      <circle cx="23" cy="23" r="20" fill="none" stroke="#1e9fd2" stroke-width="4"/>
      <path d="M17,12 L33,23 L17,34 Z"/>
    </svg>
    <div class="or" style="left:283px;top:241px">or</div>
    <svg class="set-icon" style="left:284px;top:258px" width="38" height="46" viewBox="0 0 38 46">
      <rect x="1" y="1" width="36" height="44"/>
      <rect x="9" y="4" width="20" height="17" fill="#fff"/>
      <rect x="9" y="25" width="20" height="17" fill="#fff"/>
      <g fill="#fff"><rect x="3" y="4" width="3" height="4"/><rect x="3" y="12" width="3" height="4"/><rect x="3" y="20" width="3" height="4"/><rect x="3" y="28" width="3" height="4"/><rect x="3" y="36" width="3" height="4"/>
      <rect x="32" y="4" width="3" height="4"/><rect x="32" y="12" width="3" height="4"/><rect x="32" y="20" width="3" height="4"/><rect x="32" y="28" width="3" height="4"/><rect x="32" y="36" width="3" height="4"/></g>
    </svg>
    <div class="or" style="left:283px;top:311px">or</div>
    <svg class="set-icon" style="left:280px;top:333px" width="48" height="42" viewBox="0 0 48 42">
      <rect x="2" y="4" width="30" height="18"/>
      <path d="M32,9 L46,4 V22 L32,17 Z"/>
      <path d="M17,22 L9,41 M17,22 L25,41 M17,22 V41" stroke="#1e9fd2" stroke-width="2.5"/>
    </svg>
    <div class="set-label" style="left:253px;top:383px">Videos</div>

    <svg class="set-icon" style="left:147px;top:430px" width="40" height="46" viewBox="0 0 40 46">
      <path d="M12,8 L38,2 V36 A6,5 0 1 1 34,31 V13 L16,17 V41 A6,5 0 1 1 12,36 Z"/>
    </svg>
    <div class="or" style="left:147px;top:482px">or</div>
    <svg class="set-icon" style="left:152px;top:498px" width="32" height="50" viewBox="0 0 32 50">
      <rect x="8" y="1" width="16" height="28" rx="8"/>
      <path d="M3,20 Q3,36 16,36 Q29,36 29,20" fill="none" stroke="#1e9fd2" stroke-width="3"/>
      <rect x="14" y="36" width="4" height="8"/><rect x="6" y="44" width="20" height="4"/>
    </svg>
    <div class="set-label" style="left:117px;top:553px">Audio/Music</div>

    <svg class="set-icon" style="left:53px;top:498px" width="40" height="50" viewBox="0 0 40 50">
      <rect x="1.5" y="1.5" width="37" height="47" rx="3" fill="none" stroke="#1e9fd2" stroke-width="3"/>
      <rect x="1.5" y="1.5" width="37" height="6"/>
      <rect x="8" y="14" width="24" height="24" fill="none" stroke="#1e9fd2" stroke-width="2.5"/>
      <circle cx="20" cy="22" r="4"/><path d="M12,36 Q12,28 20,28 Q28,28 28,36 Z"/>
    </svg>
    <div class="set-label" style="left:26px;top:553px">Contacts</div>

    <svg class="set-icon" style="left:235px;top:503px" width="48" height="42" viewBox="0 0 48 42">
      <g transform="translate(16,16)">
        <circle r="10"/>
        <rect x="-3" y="-15" width="6" height="30"/><rect x="-15" y="-3" width="30" height="6"/>
        <rect x="-3" y="-15" width="6" height="30" transform="rotate(45)"/><rect x="-3" y="-15" width="6" height="30" transform="rotate(-45)"/>
        <circle r="4.5" fill="#fff"/>
      </g>
      <g transform="translate(36,30)">
        <circle r="7"/>
        <rect x="-2.2" y="-10.5" width="4.4" height="21"/><rect x="-10.5" y="-2.2" width="21" height="4.4"/>
        <rect x="-2.2" y="-10.5" width="4.4" height="21" transform="rotate(45)"/><rect x="-2.2" y="-10.5" width="4.4" height="21" transform="rotate(-45)"/>
        <circle r="3" fill="#fff"/>
      </g>
    </svg>
    <div class="set-label" style="left:208px;top:553px">Setting</div>
  </section>

  <section class="screen" aria-label="Backup categories screen">
    <div class="status-bar">
      <svg width="28" height="20" viewBox="0 0 28 20" fill="#1e9fd2"><path d="M14,20 L0,6 Q14,-4 28,6 Z"/></svg>
      <svg width="12" height="20" viewBox="0 0 12 20"><rect x="3" y="0" width="6" height="3" fill="#1e9fd2"/><rect x="0" y="2" width="12" height="18" fill="#1e9fd2"/><path d="M7,4 L3,12 H6 L5,18 L9,9 H6 Z" fill="#000"/></svg>
      <span class="status-time">6:28</span>
    </div>
    <div class="action-bar">
      <div class="done">
        <svg width="34" height="26" viewBox="0 0 34 26"><path d="M2,14 L12,24 L32,2" fill="none" stroke="#fff" stroke-width="2.5"/></svg>
        DONE
      </div>
      <div class="divider"></div>
      <div class="overflow"><span></span><span></span><span></span></div>
    </div>
    <ul class="setting-list">
      <li class="setting-row">
        <div class="row-icon"><svg width="40" height="50" viewBox="0 0 40 48"><path d="M7,2 L14,2 L17,13 L12,17 Q16,29 25,36 L30,32 L39,37 L37,45 Q33,48 26,45 Q8,35 3,14 Q2,6 7,2 Z"/></svg></div>
        <span class="row-label">Calls</span>
        <div class="toggle"><div class="toggle-on">ON</div></div>
      </li>
      <li class="setting-row">
        <div class="row-icon"><svg width="40" height="50" viewBox="0 0 40 50"><rect x="1.5" y="1.5" width="37" height="47" rx="3" fill="none" stroke="#1e9fd2" stroke-width="3"/><rect x="1.5" y="1.5" width="37" height="6"/><rect x="8" y="14" width="24" height="24" fill="none" stroke="#1e9fd2" stroke-width="2.5"/><circle cx="20" cy="22" r="4"/><path d="M12,36 Q12,28 20,28 Q28,28 28,36 Z"/></svg></div>
        <span class="row-label">Contacts</span>
        <div class="toggle"><div class="toggle-on">ON</div></div>
      </li>
      <li class="setting-row">
        <div class="row-icon"><svg width="50" height="36" viewBox="0 0 50 36"><rect x="1.5" y="1.5" width="47" height="33" fill="none" stroke="#1e9fd2" stroke-width="3"/><path d="M2,3 L25,22 L48,3 M2,33 L19,17 M48,33 L31,17" fill="none" stroke="#1e9fd2" stroke-width="2.5"/></svg></div>
        <span class="row-label">Messagaes</span>
        <div class="toggle"><div class="toggle-on">ON</div></div>
      </li>
      <li class="setting-row">
        <div class="row-icon"><svg width="46" height="36" viewBox="0 0 46 36"><rect x="1" y="1" width="36" height="26" fill="none" stroke="#1e9fd2" stroke-width="2"/><rect x="8" y="8" width="37" height="27" fill="#fff" stroke="#1e9fd2" stroke-width="2"/><path d="M11,32 L21,22 L27,27 L33,20 L42,32 Z"/><circle cx="18" cy="16" r="3"/></svg></div>
        <span class="row-label">Photos</span>
        <div class="toggle"><div class="toggle-on">ON</div></div>
      </li>
      <li class="setting-row">
        <div class="row-icon"><svg width="48" height="42" viewBox="0 0 48 42"><rect x="2" y="4" width="30" height="18"/><path d="M32,9 L46,4 V22 L32,17 Z"/><path d="M17,22 L9,41 M17,22 L25,41 M17,22 V41" stroke="#1e9fd2" stroke-width="2.5"/></svg></div>
        <span class="row-label">Videos</span>
        <div class="toggle"><div class="toggle-on">ON</div></div>
      </li>
      <li class="setting-row">
        <div class="row-icon"><svg width="32" height="50" viewBox="0 0 32 50"><rect x="8" y="1" width="16" height="28" rx="8"/><path d="M3,20 Q3,36 16,36 Q29,36 29,20" fill="none" stroke="#1e9fd2" stroke-width="3"/><rect x="14" y="36" width="4" height="8"/><rect x="6" y="44" width="20" height="4"/></svg></div>
        <span class="row-label">Audio</span>
        <div class="toggle"><div class="toggle-on">ON</div></div>
      </li>
    </ul>
  </section>

  <div class="app-icon framed">
    <div class="icon-tile" role="img" aria-label="Velora backup app icon mark, framed version">
      <span class="icon-name">Velora</span>
    </div>
  </div>

  <div class="app-icon plain">
    <div class="icon-tile" role="img" aria-label="Velora backup app icon mark, plain version">
      <span class="icon-name">Velora</span>
    </div>
  </div>

</div>
</body>
</html>
```